Halvorn - Refresh the look and feel of an existing website

We currently have an existing website www.halvornworldadvisory.example however it needs a more refreshed 'look and feel'. We are a professional consultancy that works with large corporate organisations and government. Our 'tag line' is A New Way of Thinking. We want the site to communicate "Innovation" and Leading Edge Thinking.

Target Market(s)

Corporate and Professional Clients - Organisation and Business Change

Industry/Entity Type

Management Consulting

Number of Pages Required

1 page

Font styles to use
Sans Serif

Requirements
Must have
• Must have a professional Corporate look and feel. Header 'imagery' is ok but boxes on front page need changing ... along with the words. The focus on home page needs to 'call out' 3 main consulting areas:-
• - Change & Transformation Specialists
• - Innovative Solutions
• - Digital Transformation
• Tag Line for business is ... A New Way of Thinking (Highlighting Halvorn as 'Thought Leaders' in business)
Nice to have
• Less "words' more imagery. Possibly an area for a 'video' or recent articles/blogs on the front page. Needs to have more of an 'interactive' feel. We are open to suggestions.
Should not have
• NA

```html
<!DOCTYPE html>
<html lang="en">
<head>
<meta charset="utf-8">
<title>Halvorn – A New Way of Thinking</title>
<link href="https://fonts.googleapis.com/css2?family=Open+Sans:wght@400;600;700;800&display=swap" rel="stylesheet">
<style>
  :root {
    --blue: #3d97f0;
    --ink: #1b1b1b;
    --muted-head: #e8e8e8;
    --muted-text: #c4c4c4;
    --muted-btn: #ececec;
    --footer-bg: #181818;
    --footer-bar: #0b0b0b;
    --white: #ffffff;
  }
  * { margin: 0; padding: 0; box-sizing: border-box; }
  html, body { width: 1200px; height: 2190px; overflow: hidden; }
  body {
    position: relative;
    background: var(--white);
    font-family: "Open Sans", Arial, sans-serif;
    color: var(--ink);
  }
  .abs { position: absolute; }

  /* Header */
  .site-header { position: absolute; left: 0; top: 0; width: 1200px; height: 145px; background: var(--white); }
  .brand { left: 37px; top: 56px; font-size: 46px; font-weight: 400; color: var(--blue); line-height: 1; }
  .main-nav a { position: absolute; top: 76px; font-size: 19px; color: var(--ink); text-decoration: none; white-space: nowrap; }
  .nav-caret { display: inline-block; width: 0; height: 0; border-left: 6px solid transparent; border-right: 6px solid transparent; border-top: 7px solid var(--ink); margin-left: 6px; vertical-align: middle; }
  .nav-active-bar { left: 328px; top: 136px; width: 84px; height: 9px; background: var(--blue); }
  .search-icon { left: 1128px; top: 68px; }

  /* Hero */
  .hero { left: 0; top: 145px; width: 1200px; height: 363px; background: linear-gradient(100deg, #7f6e63 0%, #a8a39f 30%, #d6d4d2 55%, #c9c6c4 75%, #8a7f7a 100%); }
  .hero-shade { left: 0; top: 145px; width: 1200px; height: 363px; background: rgba(0,0,0,0.14); }
  .hero-caption { left: 300px; top: 288px; width: 600px; text-align: center; color: var(--white); font-size: 27px; line-height: 38px; }
  .btn { position: absolute; display: flex; align-items: center; justify-content: center; font-size: 16px; text-decoration: none; }
  .btn-primary { background: var(--blue); color: var(--white); }
  .btn-muted { background: var(--muted-btn); color: var(--muted-text); }
  .hero-btn { left: 526px; top: 383px; width: 146px; height: 44px; font-size: 18px; }
  .hero-arrow { top: 380px; }

  /* Service blocks */
  .block-title { position: absolute; font-size: 44px; font-weight: 800; line-height: 1; white-space: nowrap; }
  .block-title.active { color: var(--blue); }
  .block-title.muted { color: var(--muted-head); }
  .block-text { position: absolute; width: 322px; font-size: 14px; line-height: 25px; text-align: justify; }
  .block-text.active { color: var(--ink); }
  .block-text.muted { color: var(--muted-text); }
  .media { position: absolute; }

  /* Footer */
  .site-footer { left: 0; top: 1879px; width: 1200px; height: 278px; background: var(--footer-bg); }
  .footer-title { position: absolute; top: 1897px; font-size: 21px; font-weight: 700; color: var(--white); white-space: nowrap; }
  .social-dot { position: absolute; top: 1933px; width: 40px; height: 40px; border-radius: 50%; background: #3b4450; }
  .footer-links { position: absolute; left: 316px; top: 1955px; list-style: none; font-size: 18px; line-height: 23px; color: var(--white); }
  .footer-services { left: 512px; top: 1962px; width: 320px; font-size: 13px; line-height: 25px; color: var(--white); }
  .contact-line { position: absolute; font-size: 17px; color: var(--white); white-space: nowrap; }
  .copyright-bar { left: 0; top: 2157px; width: 1200px; height: 33px; background: var(--footer-bar); color: var(--white); font-size: 19px; text-align: center; line-height: 33px; }
</style>
</head>
<body>

<header class="site-header">
  <div class="abs brand">Halvorn</div>
  <nav class="main-nav">
    <a href="#" style="left:344px">Home</a>
    <a href="#" style="left:433px">About Us</a>
    <a href="#" style="left:550px">Our Services<span class="nav-caret"></span></a>
    <a href="#" style="left:696px">Solutions<span class="nav-caret"></span></a>
    <a href="#" style="left:814px">What's Happening</a>
    <a href="#" style="left:1012px">Contact Us</a>
  </nav>
  <svg class="abs search-icon" width="34" height="34" viewBox="0 0 34 34" aria-label="Search">
    <circle cx="13" cy="13" r="9" fill="none" stroke="var(--blue)" stroke-width="3.5"/>
    <line x1="20" y1="20" x2="30" y2="30" stroke="var(--blue)" stroke-width="4" stroke-linecap="round"/>
  </svg>
</header>
<div class="abs nav-active-bar"></div>

<section>
  <div class="abs hero" role="img" aria-label="Photo of a man in glasses thinking in a bright office with bookshelves"></div>
  <div class="abs hero-shade"></div>
  <p class="abs hero-caption">A New Way of Thinking —<br>thought leaders in business change</p>
  <a href="#" class="btn btn-primary hero-btn">read more</a>
  <svg class="abs hero-arrow" style="left:298px" width="20" height="34" viewBox="0 0 20 34"><polyline points="16,3 4,17 16,31" fill="none" stroke="#fff" stroke-width="3"/></svg>
  <svg class="abs hero-arrow" style="left:880px" width="20" height="34" viewBox="0 0 20 34"><polyline points="4,3 16,17 4,31" fill="none" stroke="#fff" stroke-width="3"/></svg>
</section>

<main>
  <!-- Row one -->
  <h2 class="block-title active" style="left:37px;top:582px">About Us</h2>
  <h2 class="block-title muted" style="left:440px;top:582px">What we do</h2>
  <h2 class="block-title muted" style="left:834px;top:582px">Solutions</h2>

  <div class="media" style="left:66px;top:712px;width:284px;height:186px;background:linear-gradient(90deg,#e85a3a 0%,#f2c53d 55%,#8ccf4a 100%);opacity:.85" role="img" aria-label="Illustration of green figures building a rising red and yellow bar chart"></div>
  <div class="media" style="left:447px;top:679px;width:318px;height:236px;background:radial-gradient(circle at 50% 45%,#b79a84 0%,#8d6c58 45%,#cfd3d6 100%)" role="img" aria-label="Photo of cupped hands holding soil with a small green seedling"></div>
  <div class="media" style="left:847px;top:679px;width:318px;height:236px;background:linear-gradient(120deg,#e8d6c9 0%,#a06a4e 50%,#5a3526 100%)" role="img" aria-label="Photo of two pairs of open hands reaching toward each other"></div>

  <p class="block-text active" style="left:53px;top:945px">Halvorn partners with large corporate organisations and government to lead change, shape strategy and deliver lasting results through a new way of thinking.</p>
  <p class="block-text muted" style="left:447px;top:945px">We guide organisations through business change with clear plans, strong leadership and leading edge thinking that turns bold ideas into measurable outcomes.</p>
  <p class="block-text muted" style="left:847px;top:945px">Our solutions are built around your people and processes, solving complex problems and opening new paths to growth for corporate and public clients.</p>

  <a href="#" class="btn btn-primary" style="left:53px;top:1082px;width:130px;height:41px">read more</a>
  <a href="#" class="btn btn-muted" style="left:447px;top:1082px;width:130px;height:41px">read more</a>
  <a href="#" class="btn btn-muted" style="left:847px;top:1082px;width:130px;height:41px">read more</a>

  <!-- Row two: three consulting areas -->
  <h2 class="block-title muted" style="left:50px;top:1222px">Change</h2>
  <h2 class="block-title muted" style="left:447px;top:1222px">Innovative</h2>
  <h2 class="block-title muted" style="left:845px;top:1222px">Digital</h2>

  <div class="media" style="left:53px;top:1325px;width:318px;height:235px;background:linear-gradient(160deg,#f4ece6 0%,#9cc7ea 50%,#2f78c4 80%,#f5f7f9 100%)" role="img" aria-label="Photo of a hand placing a tile into a wall of screens showing blue sky"></div>
  <div class="media" style="left:447px;top:1325px;width:318px;height:235px;background:radial-gradient(circle at 58% 60%,#c8202a 0%,#d9d9db 35%,#f2f3f5 100%)" role="img" aria-label="Illustration of white puzzle pieces with a red figure fitting the last piece"></div>
  <div class="media" style="left:847px;top:1350px;width:318px;height:236px;background:linear-gradient(135deg,#eeeeee 0%,#9c9c9c 50%,#c99a2e 75%,#5c5c5c 100%)" role="img" aria-label="Photo of a golden key resting on grey puzzle pieces"></div>

  <p class="block-text muted" style="left:53px;top:1620px">Change &amp; Transformation Specialists leading restructure, culture shift and organisation change so your teams move forward with confidence and purpose.</p>
  <p class="block-text muted" style="left:447px;top:1620px">Innovative Solutions that challenge the usual approach, pairing fresh thinking with practical delivery to unlock value across your whole business.</p>
  <p class="block-text muted" style="left:847px;top:1620px">Digital Transformation that connects strategy, systems and people, helping you adopt new technology and work smarter in a changing world.</p>

  <a href="#" class="btn btn-muted" style="left:53px;top:1756px;width:130px;height:42px">read more</a>
  <a href="#" class="btn btn-muted" style="left:447px;top:1756px;width:130px;height:42px">read more</a>
  <a href="#" class="btn btn-muted" style="left:847px;top:1756px;width:130px;height:42px">read more</a>
</main>

<footer>
  <div class="abs site-footer"></div>
  <h3 class="footer-title" style="left:39px">Connect With Us</h3>
  <span class="social-dot" style="left:55px" aria-label="Social link"></span>
  <span class="social-dot" style="left:103px" aria-label="Social link"></span>
  <span class="social-dot" style="left:151px" aria-label="Social link"></span>

  <h3 class="footer-title" style="left:318px">About Us</h3>
  <ul class="footer-links">
    <li>Our Team</li>
    <li>Our</li>
    <li>Values</li>
    <li>Giving</li>
    <li>Back</li>
  </ul>

  <h3 class="footer-title" style="left:510px">Our Services</h3>
  <p class="abs footer-services">Change &amp; Transformation Specialists, Innovative Solutions and Digital Transformation for corporate and government clients.</p>

  <h3 class="footer-title" style="left:869px">Get In Touch</h3>
  <span class="contact-line" style="left:871px;top:1950px">1300 555 010 (Aus)</span>
  <span class="contact-line" style="left:878px;top:1998px">012 555 0147 (NZ)</span>
  <span class="contact-line" style="left:878px;top:2047px">11210 555 447 (Intl)</span>
  <span class="contact-line" style="left:878px;top:2090px">info@halvornworldadvisory.example</span>

  <div class="abs copyright-bar">Copyright © 2016</div>
</footer>

</body>
</html>
```